To design the Curriculum Vitae of a General Manager Legal

the objective is to redesign the attached Résumé for a senior level Internal Legal Executive in order to make it attractive, easily readable, catchy, modern looking while staying classy, elegant, sobre, and serious.
The résumé is attached to this project. it contains the followings sections : Photo; Contact Details; Summary; Education; Experience; Other.
Feel free to use photoshop to improve photo.
Updates

Target Market(s)

Legal community; law firms; Big corporations requiring internal legal senior executive

Font styles to use
Serif

Colors
ffffff
85cae6
33a6d7
0292cd
86cfc6
cfeae6
757575
919191
d9d9d9

Requirements
Must have
• classy; serious; professional; elegant; easy to read; catchy; modern;

```html
<!DOCTYPE html>
<html lang="en">
<head>
<meta charset="utf-8">
<title>Curriculum Vitae – Page 5</title>
<link href="https://fonts.googleapis.com/css2?family=Gentium+Book+Plus:ital,wght@0,400;0,700;1,400&display=swap" rel="stylesheet">
<style>
  :root {
    --paper: #ffffff;
    --ink: #1e1e1e;
    --accent: #0292cd;
    --bullet: #85cae6;
    --side-band: #d0d0d0;
  }
  * { margin: 0; padding: 0; box-sizing: border-box; }
  html, body { width: 927px; height: 1200px; overflow: hidden; background: var(--paper); }
  body {
    position: relative;
    font-family: "Gentium Book Plus", "Palatino Linotype", serif;
    color: var(--ink);
    font-size: 15px;
    line-height: 20px;
  }
  .side-band {
    position: absolute; left: 12px; top: 12px;
    width: 32px; height: 1176px; background: var(--side-band);
  }
  .block { position: absolute; left: 110px; width: 745px; }
  .bullets { list-style: none; }
  .bullets li { position: relative; padding-left: 27px; }
  .bullets li::before {
    content: "•"; position: absolute; left: 2px; top: 0; color: var(--bullet);
  }
  .role { font-weight: 700; font-size: 14.5px; line-height: 21px; }
  .section-label { position: absolute; left: 137px; font-size: 15px; letter-spacing: .2px; }
  .school { font-weight: 700; font-size: 16px; }
  .degree em { font-style: italic; }
  .other-title {
    position: absolute; left: 0; width: 963px; text-align: center;
    color: var(--accent); font-weight: 700; font-size: 20px;
  }
  .page-number { position: absolute; left: 889px; top: 1150px; font-size: 15px; }
</style>
</head>
<body>
  <div class="side-band"></div>

  <ul class="block bullets" style="top:78px; line-height:26.5px;">
    <li>Organized hearings in international commercial arbitration.</li>
    <li>Researched work in business law, international public law and international commercial arbitration.</li>
    <li>Prepared audits.</li>
  </ul>

  <p class="block role" style="top:188px;">Mai-September, 1997&nbsp;&nbsp;&nbsp;Trainee at the law firm of Haddad, Damascus - Syria.</p>
  <ul class="block bullets" style="top:222px; line-height:26.5px;">
    <li>Activities in the field of civil, commercial and criminal law.</li>
    <li>Drafted commercial contracts.</li>
    <li>Consulted foreign companies on local laws and investment opportunities.</li>
  </ul>

  <p class="block role" style="top:333px;">June-September, 1995, 1996 Trainee at the commercial law firm of Professor Marc Darwish, Damascus – Syria.</p>
  <ul class="block bullets" style="top:387px;">
    <li>Participated at consultations in the area of commercial law.</li>
  </ul>

  <p class="section-label" style="top:433px;">EDUCATION</p>

  <p class="block school" style="top:469px;">University of Saint-Laurent Paris – France</p>
  <p class="block degree" style="top:496px;">Master degree in Litigation, Arbitration, and Alternative Dispute Resolution <em>(98-99)</em></p>
  <p class="block degree" style="top:522px;">Master degree in commercial law <em>(97-98)</em></p>
  <p class="block school" style="top:558px;">Institute of Legal Studies Paris - France (97-98)</p>
  <p class="block school" style="top:594px;">Levant National University – Syria</p>
  <p class="block degree" style="top:630px;">Law degree&nbsp; (92-96)</p>

  <h2 class="other-title" style="top:687px;">OTHER</h2>
  <ul class="block bullets" style="top:727px; line-height:26.3px;">
    <li>Nationalities: French - Syrian</li>
    <li>Married, 3 children</li>
    <li>Languages: Arabic, English, and French.</li>
    <li>Member of the Franco-Gulf Business Circle in Dubai and the Riverside Social Club</li>
    <li style="line-height:20px; padding-top:3px;">Member of various NGO’s and associations working towards Women Empowerment and education of refugee children.</li>
  </ul>

  <p class="page-number">5</p>
</body>
</html>
```